Corvath Properties Business Card Design

We would now like to design business cards with the new Corvath Properties logo

Target Market(s)

Professional

Industry/Entity Type

Professional services

Contact Information for Business Card

Employee name, title, phone number, email address, corporate office address and logo.

Font styles to use
Sans Serif

Colors
0054AA
0677BA
7BADD7
CADEEF
E8F1F8

Requirements
Must have
• My logo
Should not have
• any other pictures or images besides my logo

```html
<!DOCTYPE html>
<html lang="en">
<head>
<meta charset="utf-8">
<title>Corvath Properties Business Card</title>
<link rel="stylesheet" href="https://fonts.googleapis.com/css2?family=Montserrat:wght@400;500;700&display=swap">
<style>
  :root {
    --brand-blue: #1668d0;
    --deep-blue: #0054aa;
    --card-white: #ececec;
    --ink-faint: #dcdcdc;
    --page-bg: #f4f4f4;
    --white: #ffffff;
  }
  * { box-sizing: border-box; margin: 0; padding: 0; }
  html, body { width: 1200px; height: 840px; overflow: hidden; }
  body {
    background: var(--page-bg);
    font-family: "Montserrat", sans-serif;
    display: flex;
    flex-direction: column;
    align-items: center;
    justify-content: center;
    gap: 44px;
  }
  .card {
    position: relative;
    width: 640px;
    height: 366px;
    overflow: hidden;
    box-shadow: 0 6px 18px rgba(0,0,0,0.12);
  }

  /* Front */
  .card-front { background: var(--brand-blue); color: var(--white); }
  .front-brand {
    position: absolute;
    left: 150px;
    top: 130px;
    display: flex;
    align-items: center;
    gap: 16px;
  }
  .brand-square {
    flex: none;
    width: 46px; height: 46px;
    border: 5px solid currentColor;
  }
  .brand-name {
    font-weight: 500;
    font-size: 30px;
    letter-spacing: 1px;
  }
  .website {
    position: absolute;
    left: 150px;
    top: 222px;
    font-size: 14px;
    letter-spacing: 7px;
  }

  /* Back */
  .card-back { background: var(--card-white); color: var(--brand-blue); }
  .back-decor {
    position: absolute;
    right: -40px;
    top: 120px;
    width: 280px;
    height: 280px;
    border: 26px solid var(--ink-faint);
  }
  .back-brand {
    position: absolute;
    left: 40px;
    bottom: 52px;
    display: flex;
    align-items: center;
    gap: 14px;
  }
  .back-brand .brand-square { width: 44px; height: 44px; }
  .back-brand .brand-name {
    font-size: 24px;
    line-height: 1.15;
    display: flex;
    flex-direction: column;
  }
  .divider {
    position: absolute;
    left: 318px;
    top: 92px;
    width: 2px;
    height: 210px;
    background: var(--brand-blue);
  }
  .icon-stack {
    position: absolute;
    left: 303px;
    top: 140px;
    display: flex;
    flex-direction: column;
    gap: 14px;
  }
  .icon-box {
    width: 32px; height: 28px;
    background: var(--brand-blue);
    display: flex;
    align-items: center;
    justify-content: center;
  }
  .identity {
    position: absolute;
    left: 372px;
    top: 46px;
  }
  .person-name { font-weight: 700; font-size: 26px; }
  .person-title {
    font-size: 13px;
    letter-spacing: 12px;
    margin-top: 2px;
    padding-left: 40px;
  }
  .contact-list {
    position: absolute;
    left: 372px;
    top: 140px;
    list-style: none;
    font-size: 15px;
    display: flex;
    flex-direction: column;
    gap: 14px;
  }
  .contact-list li { line-height: 28px; height: 28px; }
</style>
</head>
<body>

  <section class="card card-front">
    <div class="front-brand">
      <span class="brand-square"></span>
      <span class="brand-name">Corvath Properties</span>
    </div>
    <p class="website">www.website.com</p>
  </section>

  <section class="card card-back">
    <div class="back-decor"></div>

    <div class="back-brand">
      <span class="brand-square"></span>
      <span class="brand-name"><span>Corvath</span><span>Properties</span></span>
    </div>

    <div class="identity">
      <p class="person-name">Your Name</p>
      <p class="person-title">TITLE</p>
    </div>

    <div class="divider"></div>

    <div class="icon-stack">
      <span class="icon-box">
        <svg width="14" height="16" viewBox="0 0 14 16"><path d="M7 0C3.4 0 1 2.6 1 5.8 1 10 7 16 7 16s6-6 6-10.2C13 2.6 10.6 0 7 0z" fill="#fff"/><circle cx="7" cy="6" r="2.3" fill="#1668d0"/></svg>
      </span>
      <span class="icon-box">
        <svg width="15" height="15" viewBox="0 0 24 24"><path d="M6.6 10.8a15.1 15.1 0 0 0 6.6 6.6l2.2-2.2c.3-.3.7-.4 1-.2 1.1.4 2.3.6 3.6.6.6 0 1 .4 1 1V20c0 .6-.4 1-1 1C10.6 21 3 13.4 3 4c0-.6.4-1 1-1h3.5c.6 0 1 .4 1 1 0 1.3.2 2.5.6 3.6.1.3 0 .7-.2 1l-2.3 2.2z" fill="#fff"/></svg>
      </span>
      <span class="icon-box">
        <svg width="16" height="12" viewBox="0 0 16 12"><rect x="0.5" y="0.5" width="15" height="11" fill="#fff"/><path d="M1 1l7 6 7-6" fill="none" stroke="#1668d0" stroke-width="1.5"/></svg>
      </span>
    </div>

    <ul class="contact-list">
      <li>ADDRESS - xxxxxxxxxxx</li>
      <li>PHONE - xxxxxxxxxxx</li>
      <li>E-MAIL - xxxxxxxxxxx</li>
    </ul>
  </section>

</body>
</html>
```